KEB Lau Sound business package.
business cards, stationary, letterhead, envelopes, CD labels and packaging, appointment cards, etc..
Thank you Mr. harven47 !!!!!
CONGRATS 7pixelcrafter
CONGRATS Mr. 7pc!!!!!!!!!!!!!!!!!!
I chose draft #56 as the winner.
I wanted to thank all designers for their great contributions and all your help and great advice.
You guys are all awesome.
I of course wanted to thank Mr. 7pc in particular from the bottom of my heart for always dealing so gracefully and friendly with my sometimes tough to deal with "Mr. Perfectionist" attitude and way of doing things. haha :)
I am super happy with the chosen design.
Fantastic work.
THANK YOU.
Much love to you and your family.
Talor.
@ PH Thank you for your honesty and candor about your likely early decision on the design. I hope all PH's can be as honest and thoughtful. Good luck with your business!!!
It looks like Mr. 7pixelcrafter's draft #48 is going to be the winner.
I know I could always be surprised of course, but I don't think anybody is going to be able to change my mind and beat how I feel about his design.
I know I still have over a day left before this project closes, but... I am only posting this here because I care about your time, talent and energy, and I want to make sure you don't spend extra time and resources on this project if you could be working on other projects where you have a higher likelihood of winning the project.
I am super anxious to see Mr. 7pixelcrafter's revisions I asked for.
My favorite designs btw are:
#20 (all the design AND the business cards), #31 (but not the business cards and not the shirts), #37 and #38
It looks like this is going to go between Mr. 7pixelcrafter and my friend who created the logo Mr. Harven47 for the winning bid.
We seem to have an India vs. India house contest here haha.
At this time: I tend to lean over to really liking #20 and #31 as my favorites.
Tips and pointers:
1) I gravitate towards preferring having the contact info at the bottom of the fax/letterhead (as in #20 and #31)
I have a feeling that the design that is going to win, is going to be the design that has the contact info at the bottom, and the company name more featured on top of the letterhead/fax design.
2) I prefer ligher colors that fit/match as closely as possible to the color of the KEB Lau Sound logo.
3) I tend to prefer having the KEB Lau Sound logo featured.. meaning: larger... on business cards, letterheads, fax pages, actually... everything.
4) I tend to lean towards liking having the big "O" with headphones logo on the lower left corner of fax/letterhead pages as a light background/watermark
5) I REALLY really like it when ALL materials have a certain design element that ties ALL materials together. Which is why I for example REALLY like #20 (ALL the materials have exactly the same design elements
6) I would LOOOOOVEEE to see copies/drafts of my 4 favorite designs mentioned above, with some slight touch of silver added to the white backgrounds of all materials/stationary. (As in the silver-ish kind of background in the original "white/silver background" of the KEB Lau Sound logo file I uploaded for this project)
Fixes:
1) I need to have the 415-738-2261 (cell) number on top of the landline (323 etc) number on all materials. (cell first)
2) I absolutely want the center of the O's in "KEB Lau Sound" to be exactly the same color as the background (on ALL materials). If the background is black, I want the center of the O to be black as well, if it is turquoise, then I want the center of the O to be turquoise as well, etc... etc...
Thank you for all your amazing work.
Much respect and love for all your work and your talent.
Best
First off:
I am SUPER HAPPY with all your submissions. You are ALL doing an amazing job and it is again going to be very hard for me to choose here. :)
So here's some guidance, sharing with you my favorite things I have seen, likes, etc...
Right now my 2 favorite ones are #33 and #31
My favorite color so far is Mr. Harven's #33
Mr Harven, Could I see a copy of the fax sheet and stationary/letterhead with the big O in the lower left corner
1) much lighter in color (kind a like a watermark. My concern is that it might interfere with typed text on the letter as it is now)
2) with that big O moved a bit to the left so the whole symbol is on the page.
3) with the company name/logo bigger on all materials.
(This does not have to be 3 different drafts btw... trying to save you time here... I am looking for one draft that has all these 3 things all together.)
More about #33
I LOVE the simplicity of the footer (bottom of page) you created on the letterhead/footer and fax page.
On the business cards: you did an amazing job on the color of the back of the business card. Keep it that way please haha. However: you know how much I am in love with color of the logo you created: is there any way you can have the logo/business name in the original color (instead of white) on that awesome background you created here?? (not sure if that would work, or if it would be too much of the same color?)
How would it look like if you made the word 'Music" black?
Mr. 7pixelcrafter draft #31
I completely LOVE how you did this smart out of the box thinking thing and made the business cards vertical (which is pretty unusual haha). So cool.
I also really frigging like what you did with the blue hue color lettering in my name and URL on the business cards.
I also adore the design of the fax sheet and letterhead. I really like it's simplicity.
But can I see a draft of the letterhead and fax page: where
1) you make a the company logo top left corner a bit bigger
2) Can you also add the O with head phones in the lower right corner, very lightly (like a watermark type thing)
Lastly: I am trying to figure out how I like the business cards with the company name in the big O.
Part of me is in love with the company logo design, and want to see it bigger and free (meaning: not surrounded by the big O ). I prefer the idea of using that O icon as a lighter background/watermark kind a thing.
Comments for everybody:
1) I need to have my cell phone number and email on the CD labels and on the CD insert sheet.
2) I would like you all to use little icons instead of using the words "cell", "address", "phone", etc...
The reason being that icons are more international: the word "cell" for example in Britain or Australia is confusing, as they call it a "mobile" there.
3) Us a little "house" icon for "address"
4) I want my cell number, to be ABOVE my land line/phone number
5) I want the address LAST. (Think about it: people have short attention spans haha... it's all about marketing and grabbing people... the FIRST thing they want to see is where to get in touch with you right now... your cell phone... not where you live.)
Draft #26 and #27
I like your very smart idea of creating tablature paper, music paper etc... with my logo and business name/logo on. You get extra points sir for that amazing idea. I should have thought of that myself already, but you beat me to it haha.
On the black shirt: I would not put the O logo on the front, as it makes it a bit too heavy and busy, already having my name logo there. I woud make the name logo bigger, and have the big O on the back of the shirt. Also: no tilted O.
On the white top: FANTASTIC artwork with the O logo... I really like the dotted approach you came up with here.
I also like how you picked up on my asking in an earlier post about the more silvery approach I wanted to see examples of.

```html
<!DOCTYPE html>
<html lang="en">
<head>
<meta charset="utf-8">
<title>KEB Lau Sound – Business Card</title>
<link rel="stylesheet" href="https://fonts.googleapis.com/css2?family=Source+Sans+3:wght@400;600;700&display=swap">
<style>
  :root {
    --backdrop: #e9e7e3;
    --card-white: #ffffff;
    --brand-blue: #1f8fd0;
    --brand-deep: #1477b8;
    --brand-light: #c3e4f4;
    --ink: #3a3a3a;
    --back-center: #5fbde9;
    --back-edge: #1a80c2;
  }
  * { margin: 0; padding: 0; box-sizing: border-box; }
  html, body { width: 1200px; height: 802px; overflow: hidden; }
  body {
    background: var(--backdrop);
    font-family: "Source Sans 3", sans-serif;
    position: relative;
  }
  .card {
    position: absolute;
    width: 540px;
    height: 310px;
    border-radius: 3px;
    box-shadow: 0 6px 18px rgba(0,0,0,0.18);
    overflow: hidden;
  }
  /* Front */
  .card-front { left: 50px; top: 90px; background: var(--card-white); }
  .front-wave { position: absolute; inset: 0; width: 100%; height: 100%; }
  .address {
    position: absolute; left: 300px; top: 28px;
    font-size: 12px; line-height: 15px; color: var(--ink);
  }
  .contact-list {
    position: absolute; left: 300px; top: 66px;
    list-style: none; font-size: 12px; line-height: 15px; color: var(--ink);
  }
  .contact-list .label { color: var(--brand-blue); font-weight: 700; margin-right: 5px; }
  .brand {
    position: absolute; left: 40px; top: 132px;
    display: flex; align-items: center; gap: 10px;
  }
  .brand-dot {
    width: 22px; height: 22px; border-radius: 50%;
    background: var(--brand-blue);
  }
  .brand-name {
    font-size: 34px; font-weight: 700; color: var(--brand-blue);
    letter-spacing: 0.5px;
  }
  .holder {
    position: absolute; left: 292px; top: 226px; color: var(--card-white);
  }
  .holder-name { font-size: 20px; font-weight: 700; }
  .holder-role { font-size: 11px; margin-top: 1px; }
  /* Back */
  .card-back {
    left: 610px; top: 400px;
    background: radial-gradient(ellipse at 50% 45%, var(--back-center) 0%, var(--back-edge) 100%);
    color: var(--card-white);
    text-align: center;
  }
  .back-circle {
    position: absolute; left: 50%; top: 92px;
    width: 62px; height: 62px; margin-left: -31px;
    border: 6px solid var(--card-white); border-radius: 50%;
  }
  .back-name {
    position: absolute; left: 0; right: 0; top: 168px;
    font-size: 20px; font-weight: 700;
  }
  .back-web {
    position: absolute; left: 0; right: 0; top: 204px;
    font-size: 12px; font-weight: 600;
  }
</style>
</head>
<body>
  <section class="card card-front">
    <svg class="front-wave" viewBox="0 0 540 310" preserveAspectRatio="none" aria-hidden="true">
      <path d="M0 232 C150 196 330 166 540 140 L540 310 L0 310 Z" fill="var(--brand-light)"/>
      <path d="M0 262 C170 224 350 196 540 176 L540 310 L0 310 Z" fill="var(--brand-blue)"/>
      <path d="M0 290 C170 262 350 240 540 226 L540 310 L0 310 Z" fill="var(--brand-deep)" opacity="0.35"/>
    </svg>
    <p class="address">P.O. Box 5816, Westbrook,<br>CA 90412, USA</p>
    <ul class="contact-list">
      <li><span class="label">p.</span>323-584-1907</li>
      <li><span class="label">c.</span>415-738-2261</li>
      <li><span class="label">e.</span>talor@keblausound.com</li>
      <li><span class="label">w.</span>www.keblausound.com</li>
    </ul>
    <div class="brand">
      <span class="brand-dot"></span>
      <span class="brand-name">KEB Lau Sound</span>
    </div>
    <div class="holder">
      <p class="holder-name">Talor R. Van Dellmore</p>
      <p class="holder-role">Musician, Instructor, Producer, Engineer</p>
    </div>
  </section>

  <section class="card card-back">
    <span class="back-circle"></span>
    <p class="back-name">KEB Lau Sound</p>
    <p class="back-web">www.keblausound.com</p>
  </section>
</body>
</html>
```